Create a Magazine Ad for an asbestos law firm

we need an 8 X 13 ad to be on the back of a magazine cover. We have the text Attached and want a similar look and feel to our website : www.harborvale-claims.example. The ad should be targeted to white males 55 years or older who are conservative and worked in industry or industrial plants. The main offer is a free case review and trying to get them to call the telephone number.

Target Market(s)

White collar men who worked in industrial plants. Age 55 years or older.

Industry/Entity Type

Legal

Requirements
Must have
• Pictures of white middle class conservative man or man and woman
Nice to have
• look at www.harborvale-claims.example to an. idea of what we are looking for

```html
<!DOCTYPE html>
<html lang="en">
<head>
<meta charset="utf-8">
<title>Mesothelioma Compensation – Magazine Ad</title>
<link href="https://fonts.googleapis.com/css2?family=Bebas+Neue&family=Roboto:ital,wght@0,400;0,500;0,700;0,900;1,400&display=swap" rel="stylesheet">
<style>
  :root{
    --page:#e9ecee;
    --paper:#ffffff;
    --ink:#111111;
    --text:#2d2d2d;
    --muted:#555555;
    --accent:#fbb400;
    --accent-text:#f5a300;
    --photo-dark:#4a4d52;
    --photo-mid:#8a8c90;
    --photo-light:#dcdde0;
  }
  *{margin:0;padding:0;box-sizing:border-box}
  html,body{width:848px;height:1200px;overflow:hidden;background:var(--page)}
  body{font-family:"Roboto",Arial,sans-serif;color:var(--text);position:relative}
  .ad{position:absolute;left:67px;top:20px;width:714px;height:1160px;background:var(--paper);overflow:hidden}
  .ad > *{position:absolute}
  .hero-photo{left:0;top:0;width:714px;height:520px;
    background:
      linear-gradient(to bottom, rgba(255,255,255,0) 55%, rgba(255,255,255,.85) 85%, #fff 100%),
      linear-gradient(to right, var(--photo-dark) 0%, var(--photo-mid) 45%, var(--photo-light) 60%, #eeeeee 80%, #c9c9c6 100%);}
  .hero-rule{left:0;top:350px;width:356px;height:3px;background:var(--accent)}
  .headline{left:23px;top:358px;font-weight:900;font-size:37px;line-height:41px;color:var(--ink);letter-spacing:-.2px}
  .intro{left:24px;top:445px;font-weight:700;font-size:18px;line-height:21px;color:#2a2a2a;width:590px}
  .bullets{left:32px;list-style:none;font-size:18.5px;line-height:27px;color:var(--text)}
  .bullets li{padding-left:21px;position:relative;white-space:nowrap}
  .bullets li::before{content:"";position:absolute;left:0;top:10px;width:7px;height:7px;border-radius:50%;background:var(--ink)}
  .bullets.sources{top:527px}
  .subhead{left:24px;top:613px;font-weight:700;font-size:18.5px;line-height:24px;color:#2a2a2a;white-space:nowrap}
  .bullets.steps{top:639px}
  .section-title{left:24px;font-weight:500;font-size:17.5px;line-height:23px;color:#222;letter-spacing:.2px}
  .section-body{left:24px;width:312px;border-left:2px solid var(--accent);padding-left:9px;font-size:11.5px;line-height:15px;color:#333}
  .trust-title{top:732px}
  .trust-body{top:779px}
  .worth-title{top:864px}
  .worth-body{top:911px}
  .settlement{font-size:11.5px;line-height:13px}
  .settlement b{display:block;font-weight:700;color:#222;margin-bottom:2px}
  .settlement i{display:block;color:var(--muted);font-size:10.5px;line-height:12px}
  .s1{left:35px;top:985px}
  .s2{left:209px;top:981px}
  .s3{left:35px;top:1038px}
  .s4{left:209px;top:1038px}
  .extra-note{left:24px;top:1093px;font-size:11.5px;line-height:14px;color:#333}
  .s5{left:35px;top:1113px}
  .eligible{left:420px;top:741px;font-family:"Bebas Neue",Impact,sans-serif;font-weight:400;font-size:38px;line-height:37px;color:var(--accent-text);width:270px}
  .evaluate{left:421px;top:866px;font-weight:500;font-size:18.5px;line-height:20.5px;color:#222;width:280px}
  .cta-band{left:401px;top:937px;width:313px;height:91px;background:var(--accent);
    font-family:"Bebas Neue",Impact,sans-serif;font-size:39px;line-height:38px;color:#222;text-align:right;padding:7px 24px 0 0}
  .call{left:421px;top:1049px;display:flex;align-items:center;gap:5px;font-weight:900;font-size:29px;line-height:30px;color:var(--accent-text)}
  .phone{left:420px;top:1086px;font-weight:900;font-size:31px;line-height:34px;color:var(--ink);letter-spacing:.5px}
  .phone-rule{left:420px;top:1125px;width:294px;height:2px;background:var(--accent)}
  .firm{right:24px;top:1142px;font-style:italic;font-size:10px;color:#444}
</style>
</head>
<body>
<main class="ad">
  <div class="hero-photo" role="img" aria-label="Photo of a grey-haired man in a white shirt working at a laptop in a home office with bookshelves and old books"></div>
  <div class="hero-rule"></div>
  <h1 class="headline">Diagnosed with Mesothelioma,<br>You could be Owed Compensation</h1>
  <p class="intro">It's very likely you developed this disease through asbestos exposure. Mesothelioma patients are getting multi-million dollar settlements, decades later, from:</p>
  <ul class="bullets sources">
    <li>Exposure to asbestos products,</li>
    <li>Ex-employers, or</li>
    <li>Talcum baby powder companies.</li>
  </ul>
  <h2 class="subhead">We can help you find out if you qualify for a case in minutes</h2>
  <ul class="bullets steps">
    <li>We'll analyze your situation at no cost</li>
    <li>Determine how much compensation you could be entitled too</li>
    <li>Show you the next steps to get what you're owed</li>
  </ul>

  <h3 class="section-title trust-title">$30 Billion is Available in<br>Trust for Mesothelioma Patients</h3>
  <p class="section-body trust-body">Tradesmen in many industries were negligently exposed to asbestos materials well into the 1990s. Whether you developed Mesothelioma yourself due to asbestos exposure or you're the surviving family of a lost loved one you could be entitled to significant compensation.</p>

  <h3 class="section-title worth-title">How much Money Can People Receive<br>from a Mesothelioma Case?</h3>
  <p class="section-body worth-body">Depending on where you were exposed and a few other factors, you can get a settlement from 6 to 7 figures. Here are a few examples of Mesothelioma Settlements received by our clients. These figures are the total</p>

  <div class="settlement s1"><b>$6,142,500</b><i>Exposed through heavy<br>duty vehicles</i></div>
  <div class="settlement s2"><b>$5,939,010</b><i>Exposed through<br>boat repair</i></div>
  <div class="settlement s3"><b>$6,033,510</b><i>Exposed through<br>general contracting</i></div>
  <div class="settlement s4"><b>$3,921,750</b><i>Exposed through<br>navy service</i></div>
  <p class="extra-note">Exposed through navy service</p>
  <div class="settlement s5"><b>$2.5 Million</b><i>Exposed from Brightwell Talcum Baby Powder.</i></div>

  <h2 class="eligible">Find out if you're eligible, for free, in minutes.!!!</h2>
  <p class="evaluate">We'll evaluate your situation and tell you what your case could be worth.</p>
  <div class="cta-band">Get your free<br>evaluation now !</div>
  <div class="call">
    <svg width="26" height="24" viewBox="0 0 26 24" aria-hidden="true">
      <path d="M2 8 C2 3 24 3 24 8 L24 10 L18 10 L18 7 L8 7 L8 10 L2 10 Z" fill="var(--accent-text)"/>
      <path d="M6 12 L20 12 L23 22 L3 22 Z" fill="var(--accent-text)"/>
      <circle cx="13" cy="17" r="3" fill="#fff"/>
    </svg>
    <span>CALL</span>
  </div>
  <p class="phone">1-XXX XXXX</p>
  <div class="phone-rule"></div>
  <p class="firm">Whitcombe &amp; Ashford, LLP, Martin Whitcombe, Lakeport, OR</p>
</main>
</body>
</html>
```